Mirela Dawn Business Card Design

I need a business card for my daughter. She has it all described in the file below. But it needs to be square in shape. http://www.mireladawn.example is her web site

Target Market(s)

18-35 year old women

Industry/Entity Type

Fashion

Contact Information for Business Card

Please look at the attached file as it has all the details.

Requirements
Must have
• Please look at the attached file as it has all the details.
Nice to have
Should not have

```html
<!DOCTYPE html>
<html lang="en">
<head>
<meta charset="utf-8">
<title>Mirela Dawn – Business Card</title>
<link href="https://fonts.googleapis.com/css2?family=EB+Garamond:wght@400&family=Mulish:wght@800&family=Bodoni+Moda:wght@700&display=swap" rel="stylesheet">
<style>
  :root {
    --frame: #111111;
    --card: #cfa6bf;
    --ink: #1a1618;
    --tag-text: #ecd6e4;
    --label: #fbf4f8;
    --icon-mark: #ffffff;
  }
  * { margin: 0; padding: 0; box-sizing: border-box; }
  html, body {
    width: 1200px;
    height: 686px;
    overflow: hidden;
    background: var(--frame);
  }
  .card {
    position: absolute;
    left: 277px;
    top: 20px;
    width: 646px;
    height: 646px;
    background: var(--card);
    overflow: hidden;
  }
  .tagline {
    position: absolute;
    left: 40px;
    top: 50px;
    width: 566px;
    height: 68px;
    background: var(--frame);
    color: var(--tag-text);
    font-family: "EB Garamond", serif;
    font-size: 30px;
    line-height: 68px;
    text-align: center;
    white-space: nowrap;
  }
  .contact {
    position: absolute;
    left: 40px;
    height: 56px;
    display: flex;
    align-items: center;
  }
  .contact-icon {
    width: 56px;
    height: 56px;
    flex: none;
  }
  .contact-text {
    margin-left: 24px;
    font-family: "Mulish", sans-serif;
    font-weight: 800;
    font-size: 28px;
    color: var(--ink);
    white-space: nowrap;
  }
  .contact--photo { top: 158px; }
  .contact--chirp { top: 230px; }
  .contact--snap  { top: 302px; }
  .contact--mail  { top: 374px; }
  .contact--mail .contact-text { margin-left: 27px; }
  .link-row {
    position: absolute;
    left: 40px;
    display: flex;
    align-items: baseline;
    white-space: nowrap;
  }
  .link-label {
    font-family: "Bodoni Moda", serif;
    font-weight: 700;
    font-size: 32px;
    letter-spacing: 2px;
    color: var(--label);
  }
  .link-value {
    font-family: "Mulish", sans-serif;
    font-weight: 800;
    font-size: 27px;
    color: var(--ink);
    margin-left: 14px;
  }
  .link-row--blog  { top: 470px; }
  .link-row--video { top: 528px; }
</style>
</head>
<body>
  <main class="card">
    <div class="tagline">blogger &amp; vlogger // beauty - fashion - travel</div>

    <div class="contact contact--photo">
      <svg class="contact-icon" viewBox="0 0 66 66" aria-hidden="true"><circle cx="33" cy="33" r="33" fill="var(--frame)"/></svg>
      <span class="contact-text">photoreel.example/mireladawnxo</span>
    </div>

    <div class="contact contact--chirp">
      <svg class="contact-icon" viewBox="0 0 66 66" aria-hidden="true"><circle cx="33" cy="33" r="33" fill="var(--frame)"/></svg>
      <span class="contact-text">chirpline.example/mireladawnxo</span>
    </div>

    <div class="contact contact--snap">
      <svg class="contact-icon" viewBox="0 0 66 66" aria-hidden="true"><circle cx="33" cy="33" r="33" fill="var(--frame)"/></svg>
      <span class="contact-text">@mireladawnxo</span>
    </div>

    <div class="contact contact--mail">
      <svg class="contact-icon" viewBox="0 0 66 66" aria-hidden="true">
        <circle cx="33" cy="33" r="33" fill="var(--frame)"/>
        <rect x="15" y="20" width="36" height="26" fill="var(--icon-mark)"/>
        <path d="M15 20 L33 35 L51 20" fill="none" stroke="var(--frame)" stroke-width="2.5"/>
        <path d="M15 46 L28 31 M51 46 L38 31" fill="none" stroke="var(--frame)" stroke-width="2"/>
      </svg>
      <span class="contact-text">mirela@mireladawn.example</span>
    </div>

    <div class="link-row link-row--blog">
      <span class="link-label">BLOG:</span>
      <span class="link-value">mireladawn.example</span>
    </div>

    <div class="link-row link-row--video">
      <span class="link-label">VLOG:</span>
      <span class="link-value">clipstream.example/mireladawn</span>
    </div>
  </main>
</body>
</html>
```